We need a redesign of our current website: www.vallowmerehosts.com. Vallowmere Holdings is a fully integrated hospitality development, management, and investment firm. We strive for leadership in each of our segments by building quality assets, exacting high standards of customer service, and focusing on returns for our investors and partners.

It is our mission to provide our guests an exceptional lodging experience; our clients an unsurpassed level of management in their properties; and create positive returns for our investors and partners. We achieve our mission via a company culture of transparency, ownership of our actions, and accountability for our results.

Target Market(s)

hotel owners, hotel developers, hotel investors, bankers

Industry/Entity Type

Hospitality

Requirements
Must have
• Our logo has to be there along with the quote and the ability to convey the following quote off of our current website: "Vallowmere was founded on the principles of integrity, honesty, loyalty, and trust. These convictions embody our company at every level, and show in every action."

```html
<!DOCTYPE html>
<html lang="en">
<head>
<meta charset="utf-8">
<title>Vallowmere Holdings — About us</title>
<link rel="stylesheet" href="https://fonts.googleapis.com/css2?family=Felipa&family=Tinos:ital,wght@0,400;0,700;1,400;1,700&family=Montserrat:wght@500&display=swap">
<style>
  :root {
    --bar: #353233;
    --paper: #ffffff;
    --ink: #111111;
    --accent-blue: #3b2fd0;
    --brand-orange: #f0891c;
    --muted: #6a6a6a;
    --rule: #c9c9c9;
    --quote-bg: rgba(40, 28, 26, 0.78);
  }
  * { margin: 0; padding: 0; box-sizing: border-box; }
  html, body { width: 1200px; height: 900px; overflow: hidden; background: var(--paper); }
  .page { position: relative; width: 1200px; height: 900px; background: var(--paper); font-family: "Tinos", "Times New Roman", serif; color: var(--ink); }
  .top-bar, .bottom-bar { position: absolute; left: 0; width: 1200px; height: 20px; background: var(--bar); }
  .top-bar { top: 0; }
  .bottom-bar { top: 880px; }

  .brand { position: absolute; left: 24px; top: 42px; display: flex; align-items: center; gap: 16px; }
  .brand-dot { width: 86px; height: 86px; border-radius: 50%; background: var(--brand-orange); }
  .brand-name { font-family: "Montserrat", sans-serif; font-weight: 500; font-size: 34px; letter-spacing: 3px; color: var(--brand-orange); line-height: 1.1; }

  .main-nav { position: absolute; top: 106px; left: 543px; display: flex; gap: 0; }
  .main-nav a { font-family: "Felipa", cursive; font-size: 27px; color: var(--ink); text-decoration: none; letter-spacing: 1.5px; }
  .main-nav a.active { color: var(--accent-blue); }
  .nav-home { position: absolute; left: 0; }
  .nav-about { position: absolute; left: 107px; white-space: nowrap; }
  .nav-hotels { position: absolute; left: 260px; }
  .nav-invest { position: absolute; left: 379px; white-space: nowrap; }
  .nav-contact { position: absolute; left: 547px; }

  .hero { position: absolute; left: 20px; top: 150px; width: 1163px; height: 302px; box-shadow: 2px 3px 3px rgba(0,0,0,0.6); overflow: hidden; }
  .hero-photo { position: absolute; inset: 0; background: linear-gradient(90deg, #cfc6b8 0%, #e9e6e1 25%, #8a4a2e 32%, #b06a44 55%, #8c4a3c 80%, #6b3a33 100%); }
  .hero-photo::after { content: ""; position: absolute; left: 0; right: 0; bottom: 0; height: 110px; background: linear-gradient(180deg, rgba(240,236,232,0) 0%, rgba(236,226,220,0.55) 60%, rgba(214,110,90,0.5) 100%); }
  .hero-quote { position: absolute; left: 57px; top: 0; width: 1050px; height: 94px; background: var(--quote-bg); color: #f4f1ee; font-family: "Felipa", cursive; font-size: 24px; letter-spacing: 2.6px; line-height: 54px; padding: 0 0 0 6px; }
  .hero-quote p { white-space: nowrap; }
  .hero-quote p:first-child { line-height: 44px; }
  .slider-dots { position: absolute; right: 16px; bottom: 15px; display: flex; gap: 10px; }
  .slider-dots span { width: 16px; height: 16px; border-radius: 50%; background: rgba(210,200,200,0.75); border: 1px solid rgba(120,110,110,0.6); }
  .slider-dots span.current { background: #555; }

  .segments { position: absolute; left: 32px; top: 500px; width: 331px; list-style: none; }
  .segments li { font-style: italic; font-size: 19px; letter-spacing: 2.4px; height: 54px; padding-top: 3px; border-bottom: 2px solid var(--rule); }
  .segments li:last-child { border-bottom: none; }
  .segments li.active { color: var(--accent-blue); }

  .about { position: absolute; left: 555px; top: 488px; width: 630px; }
  .about h2 { font-weight: 400; font-style: italic; font-size: 18px; letter-spacing: 2.5px; color: var(--accent-blue); }
  .about p { margin-top: 30px; font-weight: 700; font-style: italic; font-size: 15.5px; letter-spacing: 1.15px; line-height: 23.6px; white-space: nowrap; }

  .footer-rule { position: absolute; left: 20px; top: 805px; width: 1163px; height: 2px; background: var(--rule); }
  .footer-links { position: absolute; left: 21px; top: 834px; display: flex; gap: 18px; }
  .footer-links a { font-weight: 700; font-size: 16px; letter-spacing: 1.2px; color: var(--muted); text-decoration: none; }
  .partner { position: absolute; left: 575px; top: 826px; display: flex; align-items: center; gap: 8px; font-size: 24px; color: var(--muted); }
  .partner-mark { width: 30px; height: 30px; border-radius: 50%; background: #e8892d; }
  .copyright { position: absolute; right: 14px; top: 832px; display: flex; align-items: center; gap: 6px; font-style: italic; font-size: 16px; letter-spacing: 1.5px; color: var(--muted); }
</style>
</head>
<body>
<div class="page">
  <div class="top-bar"></div>

  <header>
    <div class="brand">
      <span class="brand-dot"></span>
      <span class="brand-name">VALLOWMERE<br>HOLDINGS</span>
    </div>
    <nav class="main-nav">
      <a class="nav-home" href="#">Home</a>
      <a class="nav-about active" href="#">About us</a>
      <a class="nav-hotels" href="#">Hotels</a>
      <a class="nav-invest" href="#">Invesment</a>
      <a class="nav-contact" href="#">Contact</a>
    </nav>
  </header>

  <section class="hero">
    <div class="hero-photo" role="img" aria-label="Hotel room interior with white bedding, red cushions and wooden lattice wall, beside framed floor plans"></div>
    <blockquote class="hero-quote">
      <p>"Vallowmere was founded on the principles of integrity,honesty, loyalty, and trust</p>
      <p>.These convictions embody our company at every level, and show in every action."</p>
    </blockquote>
    <div class="slider-dots"><span class="current"></span><span></span><span></span><span></span></div>
  </section>

  <ul class="segments">
    <li class="active">HOSPITALITY DEVELOPMENT</li>
    <li>MANAGEMENT</li>
    <li>INVESTMENT FIRM</li>
  </ul>

  <section class="about">
    <h2>ABOUT US:</h2>
    <p>Vallowmere Holdings is a fully integrated hospitality<br>
    development, management, and investment firm. We<br>
    strive for leadership in each of our segments by building quality<br>
    assets, exacting high standards of customer service, and focusing<br>
    on returns for our investors and partners. It is our mission to provide<br>
    our guests an exceptional lodging experience; our clients an<br>
    unsurpassed level of management in their properties; and create<br>
    positive returns for our investors and partners. We achieve our<br>
    mission via a company culture of transparency,<br>
    ownership of our actions, and accountability for our results.</p>
  </section>

  <div class="footer-rule"></div>
  <footer>
    <nav class="footer-links">
      <a href="#">Site map</a>
      <a href="#">Privacy Policy</a>
      <a href="#">Asseccibility</a>
    </nav>
    <div class="partner"><span class="partner-mark"></span><span>Lumaro</span></div>
    <div class="copyright">
      <svg width="24" height="24" viewBox="0 0 24 24" aria-hidden="true"><circle cx="12" cy="12" r="10.5" fill="none" stroke="#6a6a6a" stroke-width="1.5"/><path d="M15.5 9a4.5 4.5 0 1 0 0 6" fill="none" stroke="#6a6a6a" stroke-width="1.5"/></svg>
      <span>2012 Vallowmere Holdings Ltd.</span>
    </div>
  </footer>

  <div class="bottom-bar"></div>
</div>
</body>
</html>
```